We need a complete design for our construction company KELSO CONSTRUCTION based in Auckland New Zealand, we need a logo, website, business card, vehicle design etc..
We are a mid to high-end construction company who work mostly on residential projects and some commercial.

What we want to see in the design;
Professional,
Architectural,
Simple,
Alternative,

We want the design to communicate professionalism, high quality wormanship and and quality service.

Target Market(s)

People looking for a quality building/ construction company

Industry/Entity Type

Construction Company

Contact Information for Business Card

KELSO CONSTRUCTION.co.nz
Remi Tulvane
remi@kelsoconstruction-example.co.nz
021 5870 463

Logo Text

KELSO CONSTRUCTION

Number of Pages Required

5+ page

Font styles to use
Sans Serif

Colors

Designer to choose colors to be used in the design.

Requirements
Must have
• Must appear high end, professional, quality, be simple, easy to use, give security to potential clients
Nice to have
• high-quality photos of our recent projects
• about us page
• blog page
• contact us page
• high quality content
Should not have
• should not be hard to use and have too much going on.

```html
<!DOCTYPE html>
<html lang="en">
<head>
<meta charset="utf-8">
<title>Kelso Construction — Home</title>
<link rel="stylesheet" href="https://fonts.googleapis.com/css2?family=Lato:wght@400;700;900&family=Roboto:wght@300;400;500;700&display=swap">
<style>
  :root {
    --ink: #111111;
    --nav-bg: #f4f6fa;
    --text-dark: #3d3d3d;
    --text-body: #6a6a6a;
    --accent: #e8411c;
    --gold: #f5b914;
    --hero-yellow: #f7c81e;
    --button-line: #2a3b6b;
    --white: #ffffff;
  }
  * { box-sizing: border-box; margin: 0; padding: 0; }
  html, body { width: 1200px; height: 1020px; overflow: hidden; background: var(--white); }
  body { font-family: "Roboto", Arial, sans-serif; position: relative; }

  .topbar { position: absolute; left: 0; top: 0; width: 1200px; height: 50px; background: var(--ink); }
  .social { position: absolute; left: 126px; top: 12px; display: flex; gap: 16px; }
  .social span { width: 24px; height: 24px; border: 3px solid var(--gold); border-radius: 4px; display: block; }
  .phone { position: absolute; right: 128px; top: 12px; display: flex; align-items: center; gap: 12px;
    font-family: "Lato", sans-serif; font-weight: 700; font-size: 20px; letter-spacing: 3px; color: var(--white); }

  .navbar { position: absolute; left: 0; top: 50px; width: 1200px; height: 90px; background: var(--nav-bg); }
  .brand { position: absolute; left: 117px; top: 33px; display: flex; align-items: center; gap: 10px;
    font-family: "Lato", sans-serif; font-weight: 700; font-size: 21px; letter-spacing: 1.8px; color: var(--text-dark); }
  .brand-mark { width: 22px; height: 22px; background: var(--accent); }
  .menu { position: absolute; left: 519px; top: 33px; display: flex; gap: 59px; list-style: none;
    font-family: "Lato", sans-serif; font-size: 19px; letter-spacing: 1.5px; color: #555; }
  .menu .active { color: var(--gold); }

  .hero { position: absolute; left: 0; top: 140px; width: 1200px; height: 500px; }
  .hero-panel { position: absolute; left: 0; top: 0; width: 449px; height: 500px;
    background: linear-gradient(160deg, #f3c21a 0%, #f8cf2c 45%, #e8a91a 100%); }
  .hero-photo { position: absolute; left: 449px; top: 0; width: 751px; height: 500px;
    background: linear-gradient(135deg, #6a5a3c 0%, #b9ad96 35%, #a89f8a 60%, #cdb28a 80%, #8a7a60 100%); }
  .hero-copy { position: absolute; left: 95px; top: 126px; width: 330px; }
  .hero-title { font-weight: 500; font-size: 24px; color: var(--ink); letter-spacing: 0.3px; }
  .hero-rule { width: 91px; height: 5px; background: var(--accent); margin-top: 13px; }
  .hero-text { margin-top: 29px; font-size: 14px; line-height: 19.2px; letter-spacing: 1.6px; color: #2a2410; }
  .hero-actions { position: absolute; left: 101px; top: 359px; display: flex; gap: 16px; }
  .btn { height: 35px; padding: 0 16px; border: 2px solid var(--button-line); background: var(--white);
    font-size: 11px; color: var(--button-line); display: flex; align-items: center; letter-spacing: 0.2px; }

  .features { position: absolute; left: 0; top: 640px; width: 1200px; height: 380px; }
  .feature { position: absolute; top: 0; width: 280px; }
  .feature svg { position: absolute; top: 46px; }
  .feature-title { position: absolute; top: 137px; font-weight: 500; font-size: 15px; color: var(--text-dark); white-space: nowrap; }
  .feature-text { position: absolute; top: 163px; width: 280px; font-weight: 300; font-size: 12.4px; line-height: 19.3px; color: var(--text-body); }
  .read-more { position: absolute; top: 324px; right: 0; font-size: 11px; font-weight: 500; color: var(--accent); text-decoration: underline; }
</style>
</head>
<body>
  <header class="topbar">
    <div class="social" aria-label="Social links"><span></span><span></span><span></span></div>
    <div class="phone">
      <svg width="26" height="26" viewBox="0 0 24 24" aria-hidden="true"><path fill="#f5b914" d="M6.6 10.8a15.2 15.2 0 0 0 6.6 6.6l2.2-2.2a1 1 0 0 1 1-.25 11.4 11.4 0 0 0 3.6.57 1 1 0 0 1 1 1V20a1 1 0 0 1-1 1A17 17 0 0 1 3 4a1 1 0 0 1 1-1h3.5a1 1 0 0 1 1 1c0 1.25.2 2.45.57 3.57a1 1 0 0 1-.25 1z"/></svg>
      +64 21 587 0463
    </div>
  </header>

  <nav class="navbar">
    <div class="brand"><span class="brand-mark"></span>KELSO CONSTRUCTION</div>
    <ul class="menu">
      <li class="active">Home</li><li>About</li><li>Service</li><li>Blog</li><li>Contact Us</li>
    </ul>
  </nav>

  <section class="hero">
    <div class="hero-panel" role="img" aria-label="Construction tools and equipment under a warm yellow overlay"></div>
    <div class="hero-photo" role="img" aria-label="Workers cutting timber with a table saw on a building site"></div>
    <div class="hero-copy">
      <h1 class="hero-title">99 YEARS OF PASSION</h1>
      <div class="hero-rule"></div>
      <p class="hero-text">Contrary to popular belief, Lorem Ipsum is not simply random text. It has roots in a piece of classical Latin literature from 45 BC, making it over 2000 years old. Martin Ostrander, a Latin professor at Ashgrove Hill College in Vermont</p>
    </div>
    <div class="hero-actions">
      <span class="btn">LEARN&nbsp; MORE</span>
      <span class="btn">GET A QUOTE</span>
    </div>
  </section>

  <section class="features">
    <article class="feature" style="left:130px">
      <svg style="left:42px" width="80" height="70" viewBox="0 0 80 70" aria-hidden="true" fill="#e8411c">
        <circle cx="19" cy="14" r="11"/><circle cx="61" cy="14" r="11"/>
        <path d="M1 50c0-14 8-22 18-22s18 8 18 22z"/><path d="M43 50c0-14 8-22 18-22s18 8 18 22z"/>
        <circle cx="40" cy="26" r="13" stroke="#fff" stroke-width="3"/>
        <path d="M18 70c0-18 10-28 22-28s22 10 22 28z" stroke="#fff" stroke-width="3"/>
      </svg>
      <h2 class="feature-title">We are Professional team</h2>
      <p class="feature-text">There are many variations of passages of Lorem Ipsum available, but the majority have suffered alteration in some form, by injected humour, or randomised words which don't look even slightly believable. If you are going to use a passage of Lorem Ipsum, you need to be sure there isn't anything embarrassing hidden in the middle of text. All the Lorem Ipsum generators</p>
      <a class="read-more">Read more</a>
    </article>
    <article class="feature" style="left:451px">
      <svg style="left:44px" width="78" height="70" viewBox="0 0 78 70" aria-hidden="true">
        <path d="M39 66 8 35A17 17 0 0 1 39 12a17 17 0 0 1 31 23z" fill="none" stroke="#e8411c" stroke-width="4" stroke-linejoin="round"/>
      </svg>
      <h2 class="feature-title">We Build With Love</h2>
      <p class="feature-text">There are many variations of passages of Lorem Ipsum available, but the majority have suffered alteration in some form, by injected humour, or randomised words which don't look even slightly believable. If you are going to use a passage of Lorem Ipsum, you need to be sure there isn't anything embarrassing hidden in the middle of text. All the Lorem Ipsum generators</p>
      <a class="read-more">Read more</a>
    </article>
    <article class="feature" style="left:773px">
      <svg style="left:52px" width="68" height="68" viewBox="0 0 68 68" aria-hidden="true" stroke="#e8411c" fill="none" stroke-width="2">
        <circle cx="34" cy="34" r="32"/>
        <g stroke-width="2.5" stroke-linecap="round">
          <path d="M34 7v3M34 58v3M7 34h3M58 34h3M20.5 10.6l1.5 2.6M46 55l1.5 2.6M10.6 20.5l2.6 1.5M55 46l2.6 1.5M10.6 47.5l2.6-1.5M55 22l2.6-1.5M20.5 57.4l1.5-2.6M46 13l1.5-2.6"/>
        </g>
        <path d="M34 18v16h-12" stroke-width="2.5" stroke-linecap="round"/>
        <circle cx="34" cy="34" r="3"/>
      </svg>
      <h2 class="feature-title">We Deliver On The Time</h2>
      <p class="feature-text">There are many variations of passages of Lorem Ipsum available, but the majority have suffered alteration in some form, by injected humour, or randomised words which don't look even slightly believable. If you are going to use a passage of Lorem Ipsum, you need to be sure there isn't anything embarrassing hidden in the middle of text. All the Lorem Ipsum generators</p>
      <a class="read-more">Read more</a>
    </article>
  </section>
</body>
</html>
```